BrivoMatex. Lantern for the Steady Growth. Business card

Professional business card for BrivoMatex (Lantern for the Steady Growth)
My rationale: Strategy-> Execution-> Results-> Value that lead to the BrivoMatex name: We put the Lantern for the Steady Growth.
We deliver value to our customers helping them at defining a good strategy (cyan arrow). 90% of well formulated strategies fail due to poor execution so we also consider strategical execution very important (green arrow). Due to the execution we obtain the results (blue arrow). Finally, the results provide feedback to redefine strategy, and the new strategy has to be executed and new results obtained providing new feedback and on and on. It's like a wheel that finally, must create corporate value: value for shareholders, staholders, employees, providers...-

Target Market(s)

CEOs and steering comitees , invewrnent funds

Industry/Entity Type

Business Consultant

Contact Information for Business Card

Tommaso Ferlini
CEO & Founder
tommaso.ferlini@brivomatex.example
Mobile: +34 611.205.938
www.brivomatex.example

Colors

Designer to choose colors to be used in the design.

Requirements
Nice to have
• Nice to hace the words: Strategy, execution, results
• Nice to vave the claim: Lantern for the Steady Growth
• The three colors should be shown:
• cyan for STRATEGY
• green for EXECUTION
• blue for RESULTS
Should not have
• Complete black background

```html
<!DOCTYPE html>
<html lang="es">
<head>
<meta charset="utf-8">
<title>BrivoMatex – Business Card</title>
<link href="https://fonts.googleapis.com/css2?family=Lato:ital,wght@0,400;0,900;1,400&family=Nunito:wght@800&display=swap" rel="stylesheet">
<style>
  :root {
    --stage: #2b2b2d;
    --brand-blue: #233f93;
    --brand-cyan: #2aabe2;
    --brand-green: #8dc63f;
    --paper: #ffffff;
    --text-blue: #1f3a8f;
    --line-green: #c9e39c;
  }
  html, body {
    margin: 0;
    padding: 0;
    width: 1200px;
    height: 878px;
    overflow: hidden;
    background: var(--stage);
    font-family: "Lato", sans-serif;
  }
  .stage {
    position: relative;
    width: 1200px;
    height: 878px;
  }
  .card {
    position: absolute;
    left: 320px;
    width: 560px;
    height: 320px;
    box-shadow: 0 10px 24px rgba(0,0,0,.45);
    overflow: hidden;
  }

  /* Back side */
  .card-back {
    top: 99px;
    background: var(--brand-blue);
    color: var(--paper);
  }
  .card-back .brand {
    position: absolute;
    top: 118px;
    left: 0;
    right: 0;
    display: flex;
    align-items: center;
    justify-content: center;
    gap: 14px;
  }
  .brand-dot {
    width: 22px;
    height: 22px;
    border-radius: 50%;
    background: var(--paper);
  }
  .card-back .brand-name {
    font-family: "Lato", sans-serif;
    font-weight: 900;
    font-size: 50px;
    letter-spacing: -1px;
  }
  .card-back .site {
    position: absolute;
    top: 214px;
    left: 0;
    right: 0;
    text-align: center;
    font-size: 13px;
    letter-spacing: 5px;
  }

  /* Front side */
  .card-front {
    top: 459px;
    background: var(--paper);
  }
  .person {
    position: absolute;
    top: 30px;
    left: 34px;
  }
  .person-name {
    margin: 0;
    font-family: "Nunito", sans-serif;
    font-weight: 800;
    font-size: 27px;
    color: var(--text-blue);
    line-height: 1.05;
  }
  .person-role {
    margin: 0;
    font-style: italic;
    font-size: 16px;
    color: var(--brand-cyan);
  }
  .card-front .brand {
    position: absolute;
    top: 118px;
    right: 34px;
    display: flex;
    align-items: center;
    gap: 10px;
  }
  .card-front .brand-dot {
    background: var(--brand-blue);
    width: 18px;
    height: 18px;
  }
  .card-front .brand-name {
    font-weight: 900;
    font-size: 40px;
    letter-spacing: -1px;
    color: var(--text-blue);
  }
  .contacts {
    position: absolute;
    left: 34px;
    top: 166px;
    margin: 0;
    padding: 0;
    list-style: none;
    font-size: 15px;
    color: var(--brand-cyan);
  }
  .contacts li {
    display: flex;
    align-items: center;
    gap: 10px;
    height: 22px;
  }
  .icon {
    width: 14px;
    height: 14px;
    flex: none;
  }
  .divider {
    position: absolute;
    left: 34px;
    right: 34px;
    top: 238px;
    border-top: 1px solid var(--line-green);
  }
  .address {
    position: absolute;
    left: 34px;
    top: 246px;
    display: flex;
    align-items: center;
    gap: 10px;
    font-size: 15px;
    color: var(--brand-cyan);
  }
  .band {
    position: absolute;
    left: 0;
    right: 0;
    bottom: 0;
    height: 16px;
    display: flex;
    gap: 6px;
  }
  .band-cyan { width: 48px; background: var(--brand-cyan); }
  .band-blue { flex: 1; background: var(--brand-blue); }
</style>
</head>
<body>
<main class="stage">

  <section class="card card-back" aria-label="Card back">
    <div class="brand">
      <span class="brand-dot"></span>
      <span class="brand-name">BrivoMatex</span>
    </div>
    <div class="site">www.brivomatex.example</div>
  </section>

  <section class="card card-front" aria-label="Card front">
    <div class="person">
      <h1 class="person-name">Tommaso Ferlini</h1>
      <p class="person-role">Founder &amp; CEO</p>
    </div>

    <div class="brand">
      <span class="brand-dot"></span>
      <span class="brand-name">BrivoMatex</span>
    </div>

    <ul class="contacts">
      <li>
        <svg class="icon" viewBox="0 0 16 16"><path fill="#8dc63f" d="M3 1l3 3-2 2c1 2 3 4 5 5l2-2 3 3-2 3C6 14 2 10 1 3z"/></svg>
        +34 611.205.938
      </li>
      <li>
        <svg class="icon" viewBox="0 0 16 16"><rect x="1" y="3" width="14" height="10" fill="#8dc63f"/><path d="M1 3l7 6 7-6" fill="none" stroke="#fff" stroke-width="1.4"/></svg>
        tommaso.ferlini@brivomatex.example
      </li>
      <li>
        <svg class="icon" viewBox="0 0 16 16"><circle cx="8" cy="8" r="6.5" fill="none" stroke="#8dc63f" stroke-width="1.5"/><path d="M1.5 8h13M8 1.5v13M3 4.5h10M3 11.5h10" stroke="#8dc63f" stroke-width="1"/></svg>
        www.brivomatex.example
      </li>
    </ul>

    <div class="divider"></div>

    <div class="address">
      <svg class="icon" viewBox="0 0 16 16"><path fill="#8dc63f" d="M8 1a5 5 0 0 0-5 5c0 4 5 9 5 9s5-5 5-9a5 5 0 0 0-5-5zm0 7a2 2 0 1 1 0-4 2 2 0 0 1 0 4z"/></svg>
      Avda. Meridiana 214, Barcelona, 08027 España
    </div>

    <div class="band">
      <span class="band-cyan"></span>
      <span class="band-blue"></span>
    </div>
  </section>

</main>
</body>
</html>
```